Dorvanski Law Rebrand

I am recreating my law firm website. I got a new logo and would like to recreate the website to match the new logo. the website is dorvanskilaw.com

```html
<!DOCTYPE html>
<html lang="en">
<head>
<meta charset="utf-8">
<title>Dorvanski Law, PLLC</title>
<link href="https://fonts.googleapis.com/css2?family=Poppins:wght@400;500;600;700&display=swap" rel="stylesheet">
<style>
:root{
  --blue:#0b4f91;
  --blue-mid:#1f5c9e;
  --blue-soft:#7da3c6;
  --ink:#262626;
  --text:#3c3c3c;
  --grey-bg:#f1f1f1;
  --slate:#a9b6cc;
  --white:#fff;
}
*{box-sizing:border-box;margin:0;padding:0}
html,body{width:1200px;height:2886px;overflow:hidden}
body{font-family:'Poppins',sans-serif;color:var(--text);background:var(--white);position:relative}
.abs{position:absolute}
.btn{position:absolute;display:flex;align-items:center;justify-content:center;background:var(--blue);color:var(--white);font-weight:600;font-size:14px;letter-spacing:.3px;text-transform:uppercase}
.brand{color:var(--white);font-weight:600;letter-spacing:3px;display:flex;align-items:center;gap:10px;white-space:nowrap}
.brand-mark{width:14px;height:14px;border:2px solid var(--white)}

/* hero */
.hero{position:absolute;left:0;top:0;width:1200px;height:720px;overflow:hidden}
.hero-photo{position:absolute;inset:0;background:linear-gradient(120deg,#8a7a66 0%,#c8b79d 40%,#3d4f6a 70%,#1c2c45 100%)}
.hero-shade{position:absolute;inset:0}
.topbar{position:absolute;top:16px;right:74px;display:flex;gap:22px;color:var(--white);font-size:15px}
.topbar span{display:flex;align-items:center;gap:8px}
.topbar-rule{position:absolute;top:54px;left:615px;width:511px;height:1px;background:rgba(255,255,255,.35)}
.nav{position:absolute;top:80px;left:358px;display:flex;gap:40px;color:var(--white);font-size:16px}
.hero h1{position:absolute;left:74px;top:228px;width:560px;color:var(--white);font-size:45px;line-height:54px;font-weight:500}
.hero h1 b{font-weight:700}
.hero p{position:absolute;left:74px;top:402px;width:530px;color:var(--white);font-size:18.5px;line-height:30px}
.hero .btn{left:74px;top:516px;width:252px;height:45px;background:#a7b1c2;font-size:14px}

/* welcome */
.welcome h2{position:absolute;left:74px;top:828px;font-size:52px;line-height:64px;font-weight:700;color:var(--ink)}
.welcome h2 em{font-style:normal;color:var(--blue)}
.portrait{position:absolute;left:440px;top:790px;width:320px;height:320px;background:linear-gradient(180deg,#c9ccd4 0%,#3a3f4d 55%,#23283a 100%)}
.welcome-text{position:absolute;left:794px;top:832px;width:335px;font-size:15px;line-height:23.3px}
.welcome-text p+p{margin-top:12px}

/* practice */
.practice{position:absolute;left:0;top:1186px;width:1200px;height:658px;background:linear-gradient(180deg,#dbe3ee,#cdd7e4);overflow:hidden}
.practice h2{position:absolute;top:40px;width:100%;text-align:center;font-size:50px;font-weight:600;color:var(--ink)}
.practice h2 em{font-style:normal;color:var(--blue)}
.card{position:absolute;background:var(--white);box-shadow:0 2px 6px rgba(0,0,0,.05)}
.card h3{color:var(--blue);font-size:18px;font-weight:600}
.card p{font-size:13.5px;line-height:23.3px;color:var(--text)}
.card-col{text-align:center;padding:22px 16px}
.card-col h3{margin:12px 0 8px}
.card-row{padding:20px 20px 20px 92px}
.card-row h3{margin-bottom:8px}
.card-row svg{position:absolute;left:20px;top:22px}

/* blog */
.blog h2{position:absolute;left:74px;top:1900px;font-size:52px;font-weight:600;color:var(--ink)}
.blog h2 em{font-style:normal;color:var(--blue)}
.post-bg{position:absolute;background:var(--grey-bg)}
.post-img{position:absolute}
.post-body{position:absolute;width:200px}
.post-body h3{color:var(--blue);font-size:19px;line-height:31px;font-weight:600}
.post-body p{font-size:13.5px;line-height:22.5px;margin-top:6px}
.post-body a{display:inline-block;margin-top:12px;font-size:14px;color:#8a9ab5;text-decoration:underline}

/* footer */
.footer{position:absolute;left:0;top:2427px;width:1200px;height:459px;background:var(--blue);overflow:hidden}
.newsletter{position:absolute;left:74px;top:37px;width:1053px;height:121px;background:#a3b2ca}
.newsletter h2{position:absolute;left:267px;top:22px;color:var(--white);font-size:34px;font-weight:600}
.newsletter p{position:absolute;left:268px;top:70px;color:var(--white);font-size:18px}
.email{position:absolute;left:692px;top:33px;width:340px;height:57px;background:var(--white);display:flex;align-items:center;padding:0 14px;font-size:13px;color:#333;justify-content:space-between}
.fcol{position:absolute;top:2628px;color:var(--white)}
.fcol h4{font-size:17px;font-weight:600;margin-bottom:8px}
.fcol li{list-style:none;font-size:13.5px;line-height:28px}
.social{display:flex;gap:8px;margin-top:10px}
.social span{width:38px;height:38px;border:2px solid var(--white);border-radius:50%}
.copyright{position:absolute;top:2829px;left:0;width:1200px;height:57px;border-top:1px solid rgba(255,255,255,.2);color:var(--white);font-size:12.5px;text-align:center;line-height:56px}
</style>
</head>
<body>

<section class="hero">
  <div class="hero-photo" role="img" aria-label="Photo of a smiling lawyer shaking hands with a client across an office table"></div>
  <svg class="hero-shade" width="1200" height="720" viewBox="0 0 1200 720">
    <rect width="1200" height="720" fill="rgba(20,40,70,.25)"/>
    <polygon points="0,0 275,0 615,652 0,652" fill="rgba(11,79,145,.88)"/>
  </svg>
  <div class="brand abs" style="left:74px;top:72px;font-size:21px"><span class="brand-mark"></span>DORVANSKI LAW</div>
  <div class="topbar">
    <span><svg width="13" height="13" viewBox="0 0 16 16"><rect width="16" height="16" rx="3" fill="#fff"/><path d="M5 3.5l2 2-1 1.5c.7 1.4 1.6 2.3 3 3l1.5-1 2 2-1.2 1.5C7.5 12.5 3.5 8.5 3.5 4.7z" fill="#1c2c45"/></svg>(555) 014-0836</span>
    <span><svg width="15" height="12" viewBox="0 0 16 12"><rect x="1" y="1" width="14" height="10" fill="none" stroke="#fff" stroke-width="1.5"/><path d="M1 1l7 5 7-5" fill="none" stroke="#fff" stroke-width="1.5"/></svg>info@dorvanskilaw.com</span>
  </div>
  <div class="topbar-rule"></div>
  <nav class="nav"><span>Home</span><span>About Us</span><span>Practice Area</span><span>Blog</span><span>Contact</span></nav>
  <div class="btn" style="left:874px;top:68px;width:252px;height:45px">Schedule a Consultation</div>
  <h1><b>Personal Legal Solutions</b> in Life's Most Difficult Moments</h1>
  <p>Helping clients navigate probate, guardianships, estate planning, and other civil disputes by providing personal attention to each client;</p>
  <div class="btn">Schedule a Consultation</div>
</section>

<section class="welcome">
  <h2>Welcome<br>To <em>Dorvanski<br>Law, PLLC</em></h2>
  <div class="btn" style="left:75px;top:1053px;width:156px;height:45px">Read More</div>
  <div class="portrait" role="img" aria-label="Portrait of the attorney in a dark suit and red tie"></div>
  <div class="welcome-text">
    <p>It is my honor to provide quality legal services at a reasonable price to clients that I enjoy working with and for. I am grateful for all my clients and the trust they place in me to represent them.</p>
    <p>My practice focuses on Probate, Adult Guardianships, and Trust Administration and Litigation. I also represent clients in other general civil litigation matters. Finally, I handle estate planning for families of modest means.</p>
  </div>
</section>

<section class="practice" role="img" aria-label="Softly faded office interior background">
  <h2>Practice <em>Areas</em></h2>
  <div class="card card-col" style="left:74px;top:154px;width:255px;height:332px">
    <svg width="48" height="52" viewBox="0 0 48 52" fill="none" stroke="#222" stroke-width="2"><rect x="6" y="2" width="28" height="40"/><rect x="12" y="8" width="10" height="10"/><path d="M12 24h16M12 30h16M12 36h10M34 30h10M34 50h10M36 30l6 10-6 10M42 30l-6 10 6 10"/></svg>
    <h3>Probate &amp; Trusts</h3>
    <p>Guiding clients through the legal process of administering a deceased person's estate, ensuring that assets are distributed according to their wishes while addressing any legal complexities that may arise.</p>
  </div>
  <div class="card card-row" style="left:342px;top:122px;width:512px;height:188px">
    <svg width="50" height="52" viewBox="0 0 50 52" fill="none" stroke="#222" stroke-width="2"><path d="M25 2l14 6v14c0 10-7 16-14 18-7-2-14-8-14-18V8z"/><circle cx="25" cy="18" r="5"/><path d="M2 30l10 14h12M48 30l-10 14H26M12 44v6M38 44v6"/></svg>
    <h3>Adult Guardianships</h3>
    <p>Assisting families in securing legal guardianship for individuals who are unable to make decisions for themselves, ensuring that their rights and well-being are protected through compassionate and effective representation.</p>
  </div>
  <div class="card card-row" style="left:342px;top:329px;width:512px;height:189px">
    <svg width="56" height="50" viewBox="0 0 56 50" fill="none" stroke="#222" stroke-width="2"><circle cx="14" cy="8" r="5"/><circle cx="28" cy="6" r="5"/><circle cx="42" cy="8" r="5"/><path d="M4 24c0-6 4-10 10-10s10 4 10 10M18 22c0-6 4-10 10-10s10 4 10 10M32 24c0-6 4-10 10-10s10 4 10 10"/><rect x="2" y="24" width="52" height="8"/><rect x="6" y="32" width="44" height="16"/><path d="M12 38h32"/></svg>
    <h3>Civil Litigation</h3>
    <p>Representing clients in legal disputes, advocating for their rights and interests in various matters such as contract disputes, personal injury claims, and property issues, with a focus on achieving favorable outcomes through negotiation or trial.</p>
  </div>
  <div class="card card-col" style="left:872px;top:154px;width:255px;height:332px">
    <svg width="42" height="52" viewBox="0 0 42 52" fill="none" stroke="#222" stroke-width="2"><rect x="2" y="2" width="38" height="48"/><path d="M8 9h26M8 14h26M9 30l12-10 12 10M12 28v16h18V28"/><rect x="18" y="34" width="6" height="10"/></svg>
    <h3>Estate Planning</h3>
    <p>Helping individuals and families create tailored plans that safeguard their assets, ensure their wishes are fulfilled, and provide for their loved ones after they pass away.</p>
  </div>
  <div class="btn" style="left:474px;top:564px;width:252px;height:45px">Schedule a Consultation</div>
</section>

<section class="blog">
  <h2>Our <em>Blog</em></h2>
  <svg class="abs" style="left:1034px;top:1928px" width="93" height="32" viewBox="0 0 93 32">
    <path d="M4 16h28M4 16l8-6M4 16l8 6" stroke="#222" stroke-width="3" fill="none"/>
    <rect x="43" y="1" width="50" height="30" fill="#a7b1c2"/>
    <path d="M52 16h32M84 16l-8-6M84 16l-8 6" stroke="#fff" stroke-width="3" fill="none"/>
  </svg>
  <div class="post-bg" style="left:272px;top:1997px;width:315px;height:291px"></div>
  <div class="post-img" style="left:74px;top:2026px;width:268px;height:233px;background:linear-gradient(135deg,#6b5a48,#e9e6e1 60%,#b9b5ae)" role="img" aria-label="Hands signing a document beside a laptop"></div>
  <div class="post-body" style="left:362px;top:2062px">
    <h3>Trusts vs. Wills</h3>
    <p>When it comes to estate planning, two of the most common tools are trusts and wills.</p>
    <a>Learn More</a>
  </div>
  <div class="post-bg" style="left:812px;top:1997px;width:315px;height:291px"></div>
  <div class="post-img" style="left:634px;top:2026px;width:267px;height:233px;background:linear-gradient(135deg,#2b2b2b,#6a6a66 50%,#d8d4cf)" role="img" aria-label="Two people reviewing paperwork at a table"></div>
  <div class="post-body" style="left:919px;top:2047px">
    <h3>Why probate is needed,...sometime</h3>
    <p>When individuals think about estate planning, one of the first steps they often take is drafting a will.</p>
    <a>Learn More</a>
  </div>
  <div class="btn" style="left:497px;top:2330px;width:206px;height:45px">See All Blog Posts</div>
</section>

<footer class="footer">
  <svg class="abs" style="left:0;top:0" width="1200" height="459" viewBox="0 0 1200 459"><polygon points="920,0 1200,0 1200,380 783,380" fill="#2a64a4"/></svg>
  <div class="newsletter">
    <div class="brand abs" style="left:22px;top:47px;font-size:17px;letter-spacing:2.5px"><span class="brand-mark"></span>DORVANSKI LAW</div>
    <h2>Newsletter Sign Up</h2>
    <p>We Will Notify You Of Any Important News</p>
    <div class="email">Enter Email Address
      <svg width="22" height="20" viewBox="0 0 22 20"><path d="M1 9L21 1 16 19 10 12z" fill="var(--blue)"/></svg>
    </div>
  </div>
</footer>
<div class="fcol" style="left:74px"><h4>MAIN LINKS</h4><ul><li>Home</li><li>About Us</li><li>Practice Area</li><li>Blog</li><li>Contact</li></ul></div>
<div class="fcol" style="left:342px"><h4>PRACTICE AREAS</h4><ul><li>Probate and Trusts</li><li>Estate Planning</li><li>Adult Guardianships</li><li>Civil Litigation</li></ul></div>
<div class="fcol" style="left:617px"><h4>CONTACT ADDRESS</h4><ul><li style="line-height:24px">240 Meridian Avenue Suite F<br>Lakeview, Texas 77000</li><li style="margin-top:6px">(555) 014-0836</li><li style="margin-top:6px">Mon - Fri&nbsp; 8AM - 5PM</li></ul></div>
<div class="fcol" style="left:884px"><h4>CONNECT US</h4><div class="social" aria-label="Social media links"><span></span><span></span><span></span><span></span></div></div>
<div class="copyright">© 2025 Dorvanski Law, PLLC | All Rights Reserved</div>

</body>
</html>
```